Virtual Reality medical education company

We are a new company that is offering virtual reality medical simulation suites. I have had a go at the initial web design www.brellowanstudio-example.com but as you can see I am no web designer!
I have the logo and some text which I'd like you to use - also some images. Any help with the SEO would be appreciated.

Target Market(s)

Students and faculty in medical and applied medical degrees

Industry/Entity Type

Education

Coding

Coded - Design and coding required

Number of Pages Required

5+ page

Font styles to use
Sans Serif

Requirements
Must have
• Home, Benefits, Simulation, Why Virtual, Modules, Contact Us
• Virtual reality scenes, either people using it or what they see.
• This is the patient we are using http://www.plexomarket-example.com/3d-models/rigged-hospital-patient-3d-max/4830291
Nice to have
• QRN Lumo or Pentara Drift headsets being worn
Should not have
• Non VR simulation, real patients/models, students looking at computer screens

```html
<!DOCTYPE html>
<html lang="en">
<head>
<meta charset="utf-8">
<title>Veridan Medical Coaching</title>
<link href="https://fonts.googleapis.com/css2?family=Open+Sans:wght@400;600&display=swap" rel="stylesheet">
<style>
:root{
  --navy:#0c1a86;
  --band:#1b2f9e;
  --sky:#47a6dc;
  --grey-btn:#9a9a9a;
  --card:#f3f3f3;
  --text:#333;
  --muted:#666;
  --footer:#1b1b1b;
}
*{margin:0;padding:0;box-sizing:border-box}
html,body{width:862px;height:1200px;overflow:hidden;background:#fff}
body{position:relative;font-family:"Open Sans",sans-serif;color:var(--text)}
.abs{position:absolute}
.brand{left:72px;top:30px;width:170px;text-align:center;color:var(--navy);font-size:15px;font-weight:400;line-height:17px;letter-spacing:1px}
.brand-mark{display:block;width:26px;height:26px;border-radius:50%;background:var(--navy);margin:0 auto 6px}
.email{right:72px;top:22px;font-size:11px;color:#777}
.rule{left:362px;top:50px;width:428px;height:1px;background:#ddd}
.nav{top:69px;left:0;width:862px;font-size:11px;color:#555}
.nav span{position:absolute;white-space:nowrap}
.nav .on{color:var(--navy);font-weight:600}
.hero{left:0;top:102px;width:862px;height:392px;background:var(--band)}
.slide{left:71px;top:122px;width:719px;height:350px;border:2px solid #8aa0d8;background:linear-gradient(160deg,#c9c6b0 0%,#b9c3c6 45%,#9aa9ad 100%)}
.arrow{top:286px;width:34px;height:34px;background:rgba(30,30,30,.8)}
.caption{left:110px;top:402px;width:299px;height:40px;background:rgba(90,170,220,.85);color:#fff;font-size:24px;line-height:40px;padding-left:13px;white-space:nowrap}
.section-title{top:522px;left:0;width:862px;text-align:center;color:var(--navy);font-size:19px;font-weight:600}
.intro{top:563px;left:60px;width:742px;text-align:center;font-size:9px;line-height:14.2px;color:#444}
.btn{height:26px;line-height:26px;text-align:center;color:#fff;font-size:9.5px;border-radius:2px}
.btn-navy{background:var(--navy);border-bottom:2px solid #08104f}
.btn-sky{background:var(--sky);border-bottom:2px solid #2f86ba}
.btn-grey{background:var(--grey-btn);border-bottom:2px solid #7b7b7b}
.card{top:705px;width:224px;height:324px;background:var(--card)}
.card-img{position:absolute;left:8px;top:6px;width:208px;height:163px}
.card h3{position:absolute;left:0;top:178px;width:224px;text-align:center;color:var(--navy);font-size:15px;font-weight:600;line-height:14.5px}
.card p{position:absolute;left:8px;width:208px;text-align:center;font-size:9px;line-height:12.3px;color:#444}
.card .btn{position:absolute;left:68px;top:297px;width:89px}
.footer{left:0;top:1090px;width:862px;height:110px;background:var(--footer)}
.flinks{left:72px;top:1129px;font-size:9px;color:#ddd;white-space:nowrap}
.flinks .on{color:var(--sky)}
.flinks i{font-style:normal;margin:0 12px}
.copy{left:72px;top:1153px;font-size:9px;color:#ddd}
.social{left:648px;top:1128px}
</style>
</head>
<body>
<header>
  <div class="abs brand"><span class="brand-mark"></span>VERIDAN MEDICAL<br>COACHING</div>
  <div class="abs email">&#9993; Mara.Olsted@veridanmedical-example.com</div>
  <div class="abs rule"></div>
  <nav class="abs nav">
    <span class="on" style="left:390px">Home</span>
    <span style="left:446px">Benefits</span>
    <span style="left:511px">Simulation</span>
    <span style="left:588px">Why Virtual</span>
    <span style="left:670px">Modules</span>
    <span style="left:737px">Contact Us</span>
  </nav>
</header>

<section class="abs hero"></section>
<div class="abs slide" role="img" aria-label="Virtual reality scene of a patient lying on an X-ray table in a simulated radiography room"></div>
<div class="abs arrow" style="left:72px"><svg width="34" height="34"><path d="M19 12l-5 5 5 5" stroke="#fff" stroke-width="2" fill="none"/></svg></div>
<div class="abs arrow" style="left:755px"><svg width="34" height="34"><path d="M15 12l5 5-5 5" stroke="#fff" stroke-width="2" fill="none"/></svg></div>
<div class="abs caption">Veridan Medical Coaching</div>

<h2 class="abs section-title">Why Virtual</h2>
<p class="abs intro">The element of interaction is of utmost importance to make the user really feel free to<br>get involved with the virtual environment. According to Tallmark Review magazine the virtual reality (VR) market is expected to grow to US$407.51 million and reach more than<br>25 million users by 2018. This increased demand is attributed to industries that are starting to see the potential for VR products outside of the gaming world.<br>Education is one of these industries, especially in the STEM subjects, science, technology, engineering, and mathematics.</p>
<div class="abs btn btn-navy" style="left:351px;top:639px;width:78px">Read More</div>
<div class="abs btn btn-sky" style="left:433px;top:639px;width:78px">Contact</div>

<article class="abs card" style="left:71px">
  <div class="card-img" role="img" aria-label="Illustration of a clinician reassuring a patient in a hospital bed" style="background:linear-gradient(135deg,#f6f6f8,#dfe6ee)"></div>
  <h3>The Patient</h3>
  <p style="top:215px">Veridan Medical Coaching has created different patients to reflect the different sizes and genders that students will be working within the clinical environment. As you can see, the model is very realistic. The patient is fully adjustable and all positions...</p>
  <div class="btn btn-sky">Read More</div>
</article>
<article class="abs card" style="left:319px">
  <div class="card-img" role="img" aria-label="Digital radiography table with overhead tube and wall stand" style="background:linear-gradient(135deg,#fafafa,#e4e6e8)"></div>
  <h3 style="top:178px">Exposure setting and<br>imaging</h3>
  <p style="top:215px">Just like the clinical environment, imaging is conducted from behind a lead glass window which the student has to walk behind to access the console unit. The console unit has preset exposures, just like a clinical unit, which gives average...</p>
  <div class="btn btn-grey">Read More</div>
</article>
<article class="abs card" style="left:566px">
  <div class="card-img" role="img" aria-label="Close view of a radiography detector arm" style="background:linear-gradient(135deg,#b9bcbf,#e8e9ea 60%,#cfd3d5)"></div>
  <h3>Equipment</h3>
  <p style="top:221px">Veridan Medical Coaching offers the latest computed radiography (CR) and direct digital radiography (DDR) equipment. This reflects what the students will be using in the clinical environment during their training and when they graduate.</p>
  <div class="btn btn-grey">Read More</div>
</article>

<footer class="abs footer"></footer>
<div class="abs flinks"><span class="on">Home</span><i>|</i>Benefits<i>|</i>Simulation<i>|</i>Why Virtual<i>|</i>Modules<i>|</i>Contact Us</div>
<div class="abs copy">Copyright © 2016 Veridan Medical Coaching</div>
<svg class="abs social" width="150" height="34" aria-label="Social links">
  <circle cx="16" cy="16" r="16" fill="#3f64a6"/>
  <circle cx="53" cy="16" r="16" fill="#3fa0cf"/>
  <circle cx="90" cy="16" r="16" fill="#d9312c"/>
  <circle cx="126" cy="16" r="16" fill="#3fb2e6"/>
</svg>
</body>
</html>
```